High End, Contemporary Fitness Boutique 3 Panel Brochure

I have included the copy and images needed; I'm definitely no designer so it's laughable in its current state. What I'm in need of is for somebody to take the current idea and copy, and turn it into a polished high-end brochure to help educate clients and markets before a studio opens. So the copy is set, but placement (within each panel) and font, colors, design, etc are all up to you! I need your help! Thanks for checking out this project, I'll be guaranteeing this as soon as I get something back that I like, before we begin fine-tuning the design. Also, if there are any spelling or grammar changes you'd like to see, I'm open to that.

Target Market(s)

Upscale Coastal Women, 30-55, with desposible income

Industry/Entity Type

Boutique

Colors
fdf9cf
ffffff
cee9f5

Requirements
Must have
• the Blue Color is Pantone 630C, Grey is Panton 430C, I don't have a Pantone for the Yellow, I'm still looking for something soft, appealing, upmarket, and splashy to contrast (in limited supply) the Blue(630C)
Nice to have
• Uniform Look & Feel, page-turning design
Should not have
• goofy splashy graphics or fonts, salesey pitch pieces

```html
<!DOCTYPE html>
<html lang="en">
<head>
<meta charset="utf-8">
<title>FormHaven Brochure</title>
<link href="https://fonts.googleapis.com/css2?family=Lato:ital,wght@0,400;0,700;0,900;1,400&family=Oswald:wght@300;400&family=Satisfy&display=swap" rel="stylesheet">
<style>
  :root {
    --blue: #55c2dc;
    --blue-deep: #2f9fc0;
    --blue-soft: #9fdcec;
    --teal-ink: #2f6f84;
    --grey: #575b5f;
    --grey-dark: #45484b;
    --ink: #3b3d40;
    --text: #6a6d70;
    --paper: #ffffff;
    --stage: #ece9e4;
  }
  * { margin: 0; padding: 0; box-sizing: border-box; }
  html, body { width: 875px; height: 1200px; overflow: hidden; }
  body { background: var(--stage); font-family: "Lato", sans-serif; color: var(--text); position: relative; }

  .spread { position: absolute; left: 40px; width: 795px; height: 566px; overflow: hidden; box-shadow: 0 4px 14px rgba(0,0,0,.25); }
  .spread--outside { top: 24px; }
  .spread--inside { top: 610px; }
  .spread > svg.shapes { position: absolute; left: 0; top: 0; }
  .abs { position: absolute; }

  .script { font-family: "Satisfy", cursive; font-weight: 400; }
  .photo { position: absolute; }

  /* brand lockup */
  .brand { position: absolute; text-align: center; width: 265px; }
  .brand__name { display: inline-flex; align-items: center; gap: 6px; font-family: "Lato", sans-serif; font-weight: 900; color: var(--blue); letter-spacing: .5px; }
  .brand__mark { display: inline-block; background: var(--blue); }
  .brand__tag { font-size: 8px; font-weight: 700; color: var(--grey); margin-top: 1px; }

  /* outside: left panel */
  .promo-head { left: 0; top: 8px; width: 265px; text-align: center; }
  .promo-head__line { font-family: "Oswald", sans-serif; font-weight: 400; font-size: 19px; color: var(--ink); line-height: 1.2; }
  .promo-head__script { font-size: 26px; color: var(--blue); line-height: 1.15; }
  .label { font-family: "Lato", sans-serif; font-size: 11px; font-weight: 700; color: var(--ink); }
  .checklist { left: 0; width: 160px; top: 352px; text-align: center; font-size: 11px; line-height: 1.3; color: var(--ink); list-style: none; }
  .checklist li::before { content: "\221A\00a0"; }
  .quote { left: 14px; top: 424px; width: 245px; font-style: italic; font-size: 13px; color: var(--ink); line-height: 1.2; }
  .quote__mark { color: var(--blue); font-size: 17px; line-height: 1; }
  .quote__by { font-family: "Satisfy", cursive; color: var(--blue); font-style: normal; font-size: 14px; }
  .story { left: 18px; top: 468px; width: 238px; font-size: 9.4px; line-height: 1.28; color: var(--text); }

  /* outside: middle panel */
  .address { left: 290px; top: 158px; width: 215px; text-align: center; font-size: 9.5px; font-weight: 700; color: var(--grey); line-height: 1.3; }
  .hours { left: 305px; top: 205px; width: 200px; font-size: 12px; color: var(--ink); border-collapse: collapse; }
  .hours td { padding: 2px 0; height: 21px; }
  .hours .day { white-space: nowrap; }
  .tagline { left: 300px; top: 400px; width: 205px; text-align: right; font-size: 17px; color: var(--teal-ink); line-height: 1.5; white-space: nowrap; }

  /* outside: right panel */
  .slogan { left: 530px; top: 282px; width: 252px; text-align: right; color: var(--blue); line-height: 1.05; }
  .slogan__big { font-family: "Satisfy", cursive; font-size: 36px; }
  .slogan__small { font-family: "Lato", sans-serif; font-size: 12px; color: #fff; }
  .slogan__small--strong { font-size: 15px; font-weight: 900; }
  .offer { left: 530px; top: 470px; width: 265px; text-align: center; color: #fff; }
  .offer__line { font-family: "Lato", sans-serif; font-weight: 900; font-size: 21px; letter-spacing: .3px; text-shadow: 0 1px 2px rgba(0,0,0,.25); margin-top: 8px; }
  .offer__price { font-family: "Satisfy", cursive; font-size: 32px; line-height: 1.3; white-space: nowrap; }

  /* inside */
  .section-title { font-family: "Satisfy", cursive; font-weight: 400; color: var(--teal-ink); text-align: center; font-size: 29px; line-height: 1.1; white-space: nowrap; }
  .body-copy { font-size: 10.4px; line-height: 1.33; text-align: justify; color: var(--text); }
  .live-title { left: 20px; top: 76px; width: 232px; text-align: right; font-family: "Satisfy", cursive; font-weight: 400; color: var(--blue-deep); font-size: 31px; line-height: 1.15; }
  .live-copy { left: 8px; top: 152px; width: 252px; font-size: 9.6px; }
  .live-quote { left: 8px; top: 236px; width: 255px; font-style: italic; font-size: 12.5px; color: var(--ink); }
  .live-quote span { font-family: "Satisfy", cursive; font-style: normal; font-size: 14px; color: var(--ink); }
  .closing { left: 548px; top: 423px; width: 235px; font-style: italic; font-size: 13.5px; color: var(--ink); line-height: 1.35; }
</style>
</head>
<body>

<!-- Outside spread -->
<section class="spread spread--outside">
  <svg class="shapes" width="795" height="566" viewBox="0 0 795 566" aria-hidden="true">
    <defs>
      <linearGradient id="midPanel" x1="0" y1="0" x2="1" y2="0">
        <stop offset="0" stop-color="#ffffff"/><stop offset="1" stop-color="#d6d8da"/>
      </linearGradient>
      <linearGradient id="blueFade" x1="0" y1="0" x2="1" y2="1">
        <stop offset="0" stop-color="#b6e5f1"/><stop offset="1" stop-color="#45b4d3"/>
      </linearGradient>
      <linearGradient id="greyPanel" x1="0" y1="0" x2="1" y2="1">
        <stop offset="0" stop-color="#777a7d"/><stop offset="1" stop-color="#4a4d50"/>
      </linearGradient>
      <linearGradient id="offerBand" x1="0" y1="0" x2="1" y2="0">
        <stop offset="0" stop-color="#46b5d4"/><stop offset="1" stop-color="#8fd6ea"/>
      </linearGradient>
    </defs>
    <rect x="0" y="0" width="265" height="566" fill="#ffffff"/>
    <rect x="0" y="0" width="265" height="5" fill="#55c2dc"/>
    <rect x="265" y="0" width="265" height="566" fill="url(#midPanel)"/>
    <path d="M530 303 C455 340 310 430 280 566 L530 566 Z" fill="url(#blueFade)"/>
    <path d="M270 566 C300 430 450 335 530 295" fill="none" stroke="#55595d" stroke-width="7"/>
    <rect x="530" y="0" width="265" height="566" fill="url(#greyPanel)"/>
    <path d="M752 0 C790 120 792 320 770 462" fill="none" stroke="#55c2dc" stroke-width="5"/>
    <rect x="530" y="455" width="265" height="4" fill="#ffffff" opacity=".85"/>
    <rect x="530" y="462" width="265" height="104" fill="url(#offerBand)"/>
  </svg>

  <!-- left panel -->
  <header class="abs promo-head">
    <p class="promo-head__line">Lose that 10, 15, 20 lbs OR MORE..</p>
    <p class="promo-head__script script">in just 3 quick months!!</p>
  </header>
  <span class="abs label" style="left:28px;top:90px;">BEFORE</span>
  <span class="abs label" style="left:148px;top:86px;">AFTER</span>
  <div class="photo" role="img" aria-label="Before photo: woman in a taupe tank top and jeans" style="left:24px;top:106px;width:112px;height:186px;background:linear-gradient(180deg,#f4f1ee,#b9aea4 55%,#3d4a63);"></div>
  <div class="photo" role="img" aria-label="After photo: slimmer woman in a black top and blue jeans" style="left:140px;top:100px;width:110px;height:318px;background:linear-gradient(180deg,#f6f6f6,#2b2b2d 35%,#2c3e5c 70%,#e9e9e9);"></div>
  <div class="brand" style="left:-52px;top:306px;">
    <span class="brand__name" style="font-size:13px;"><span class="brand__mark" style="width:9px;height:9px;"></span>FORMHAVEN</span>
    <p class="brand__tag" style="font-size:6px;">Personal Training for Women</p>
  </div>
  <ul class="abs checklist">
    <li>Toning</li><li>Cardio Intervals</li><li>Nutrition</li><li>Consistency!</li>
  </ul>
  <p class="abs quote"><span class="quote__mark">&ldquo;</span> I lost 40lbs,<br>&nbsp;&nbsp;and nearly 12% body fat!<span class="quote__mark">&rdquo;</span> <span class="quote__by">~Dana R.</span></p>
  <p class="abs story">By incorporating the 4 Pillars of the FormHaven Program into her life for just 12 weeks, Dana found that the weight came off easier than it went on! Not only did she find that her clothes fit her better, she had so much more energy to keep up with her kids, and fit in everything else she wanted to do with her time!</p>

  <!-- middle panel -->
  <div class="brand" style="left:265px;top:96px;">
    <span class="brand__name" style="font-size:19px;"><span class="brand__mark" style="width:12px;height:12px;"></span>FORMHAVEN</span>
    <p class="brand__tag" style="font-size:7.5px;">Personal Training for Women</p>
  </div>
  <p class="abs address">
    <svg width="8" height="10" viewBox="0 0 8 10" aria-hidden="true"><path d="M4 0a4 4 0 0 1 4 4c0 3-4 6-4 6S0 7 0 4a4 4 0 0 1 4-4z" fill="#55c2dc"/><circle cx="4" cy="4" r="1.5" fill="#fff"/></svg>
    48 Harbor View Lane, Seacliff Heights
  </p>
  <table class="abs hours">
    <tr><td class="day">Monday ................. 6a-12p &amp; 4p-8p</td></tr>
    <tr><td class="day">Tuesday ................ 6a-12p &amp; 4p-8p</td></tr>
    <tr><td class="day">Wednesday ........... 6a-12p &amp; 4p-8p</td></tr>
    <tr><td class="day">Thursday ............... 6a-12p &amp; 4p-8p</td></tr>
    <tr><td class="day">Friday ................... 6a-12p</td></tr>
    <tr><td class="day">Saturday ............... 6a-12p</td></tr>
  </table>
  <p class="abs tagline script">Strength<br>Balance &amp; Energy<br>for the Best of Your Life</p>

  <!-- right panel -->
  <div class="photo" role="img" aria-label="Faint portrait of a smiling woman in white athletic wear" style="left:530px;top:0;width:190px;height:440px;background:radial-gradient(ellipse at 40% 35%,rgba(255,255,255,.55),rgba(255,255,255,.15) 55%,rgba(255,255,255,0) 80%);"></div>
  <div class="brand" style="left:530px;top:92px;">
    <span class="brand__name" style="font-size:23px;"><span class="brand__mark" style="width:14px;height:14px;"></span>FORMHAVEN</span>
    <p class="brand__tag" style="font-size:8.5px;color:#e3e5e6;">Personal Training for Women</p>
  </div>
  <div class="abs slogan">
    <p><span class="slogan__big">Lose</span> <span class="slogan__small">the weight..</span></p>
    <p><span class="slogan__big">Gain</span> <span class="slogan__small">the strength..</span></p>
    <p><span class="slogan__big">Balance</span> <span class="slogan__small slogan__small--strong">your life!!</span></p>
  </div>
  <div class="abs offer">
    <p class="offer__line">For as Little as</p>
    <p class="offer__price">$15 Per Session!</p>
  </div>
</section>

<!-- Inside spread -->
<section class="spread spread--inside">
  <svg class="shapes" width="795" height="566" viewBox="0 0 795 566" aria-hidden="true">
    <defs>
      <linearGradient id="insideMid" x1="0" y1="0" x2="1" y2="0">
        <stop offset="0" stop-color="#fbfbfb"/><stop offset="1" stop-color="#e2e3e4"/>
      </linearGradient>
      <linearGradient id="insideRight" x1="0" y1="0" x2="1" y2="0">
        <stop offset="0" stop-color="#f6f6f6"/><stop offset="1" stop-color="#e4e5e6"/>
      </linearGradient>
      <linearGradient id="topBand" x1="0" y1="0" x2="1" y2="0">
        <stop offset="0" stop-color="#4fb9d7"/><stop offset="1" stop-color="#7fd0e6"/>
      </linearGradient>
      <linearGradient id="bottomBand" x1="0" y1="0" x2="1" y2="0">
        <stop offset="0" stop-color="#7b7e81"/><stop offset="1" stop-color="#54575a"/>
      </linearGradient>
    </defs>
    <rect x="0" y="0" width="265" height="566" fill="#ffffff"/>
    <rect x="265" y="0" width="265" height="566" fill="url(#insideMid)"/>
    <rect x="530" y="0" width="265" height="566" fill="url(#insideRight)"/>
    <path d="M0 0 H795 V20 C520 22 250 36 0 88 Z" fill="url(#topBand)"/>
    <path d="M0 100 C250 46 520 30 795 28" fill="none" stroke="#55595d" stroke-width="6"/>
    <path d="M0 545 C300 550 600 522 795 452 V566 H0 Z" fill="url(#bottomBand)"/>
    <path d="M240 546 C500 540 690 500 795 432" fill="none" stroke="#55c2dc" stroke-width="5"/>
  </svg>

  <!-- left panel -->
  <h2 class="abs live-title">Live<br>your life in</h2>
  <p class="abs body-copy live-copy">Laura was able to lose over 25lbs, and just completed her first 10K race! The 4 Pillars of the FormHaven Program proved that even though she was never active or athletic before, her Top Tier Trainers showed her the way to live the fittest and healthiest life for herself and her family!</p>
  <p class="abs live-quote">If I could do it, so can YOU! <span>~Laura P.</span></p>
  <div class="photo" role="img" aria-label="Smiling woman in a pink t-shirt holding out the waist of her old oversized jeans" style="left:62px;top:262px;width:190px;height:276px;background:linear-gradient(180deg,#f7f7f7,#e9738f 40%,#4a4b50 75%,#dcdcdc);"></div>

  <!-- middle panel -->
  <h2 class="abs section-title" style="left:265px;top:46px;width:265px;">Toning!</h2>
  <p class="abs body-copy" style="left:282px;top:92px;width:234px;">Working with one of our Top Tier Personal Trainers, you will perform a complete &amp; thorough functional training workout to start each session, that will strengthen your muscles and joints, elevate your poise &amp; posture, and activate all that beautiful Metabolically Active Tissue (Muscle Tone!). The advantage of your Toning Exercises is that your body requires more fuel to move that added muscle-tone! So the same tasks you perform today, will require more calories to perform tomorrow! WOW!</p>
  <h2 class="abs section-title" style="left:265px;top:264px;width:265px;">Cardio Intervals!</h2>
  <p class="abs body-copy" style="left:282px;top:307px;width:234px;">Cardio is important for so many reasons; Heart Health, Lung Health, Circulation.. But the tangible benefit is Fat Burning! We take Cardio a step further; our Top Tier Trainers work with you on Ellipticals, Treadmills and Bikes to perform specifically designed intervals of high and low cardio effort suited to your baseline! This essentially plays a trick on your body, revving your metabolism to a point where you reach that 'afterburn' (see: EPOC). This metabolic state burns the calories as if you were to continue running for an additional two hours, WOW!</p>

  <!-- right panel -->
  <h2 class="abs section-title" style="left:530px;top:42px;width:265px;">Nutrition!</h2>
  <p class="abs body-copy" style="left:546px;top:82px;width:236px;">The most important pillar of your successful transformation is understanding nutrition's role in the program. Our Top Tier Trainers will guide you through understanding energy, and how to time the foods you love, so that they work for you, and not against you! We provide nutrition counseling, helpful meal prep tips, delicious family recipes that will become dinner table favorites, and snacks that will keep you from raiding the pantry late at night!</p>
  <h2 class="abs section-title" style="left:530px;top:240px;width:265px;">Consistency!</h2>
  <p class="abs body-copy" style="left:546px;top:288px;width:236px;">The above pillars of the FormHaven Program are vital on their own, but the real difference comes when you string them together in a consistent schedule, week after week! Our Top Tier Trainers and Studio Consultants work with you through each of these pillars to hold you accountable to maintaining your consistency, so you see the results you are working for.</p>
  <p class="abs closing">Our team is dedicated to you, and your results.</p>
</section>

</body>
</html>
```